Business Card Design

We would like a business card that utilizes our current logo and keeps with the same feel - elegant and organic. Our farm isn't about mass production, it's about excellence, education, beautiful events and flowers - people, culture, and community.

Target Market(s)

Patrons to our farm who are interested in weddings, events, or our flowers and vegetables.

Contact Information for Business Card

Name, address, cell email (Danielle Hoskins, 2716 Wrenfield Rd, Alder Springs, CO 80544, cell 30.412.6638, email danielle@wrenfieldacres.com)

```html
<!DOCTYPE html>
<html lang="en">
<head>
<meta charset="utf-8">
<title>Wrenfield Acres – Business Card</title>
<link rel="stylesheet" href="https://fonts.googleapis.com/css2?family=Montserrat:wght@700;800&display=swap">
<style>
  :root {
    --page: #ffffff;
    --card: #e8e8e8;
    --sage: #768a76;
    --sage-soft: #8a9c8a;
    --shadow: rgba(0, 0, 0, 0.22);
  }
  * { margin: 0; padding: 0; box-sizing: border-box; }
  html, body {
    width: 942px;
    height: 1200px;
    overflow: hidden;
    background: var(--page);
    font-family: "Montserrat", Arial, sans-serif;
  }
  .canvas {
    position: relative;
    width: 942px;
    height: 1200px;
  }
  .card {
    position: absolute;
    width: 860px;
    height: 438px;
    background: var(--card);
    overflow: hidden;
    box-shadow: 0 22px 26px -14px var(--shadow);
  }
  .card--front { left: 40px; top: 102px; }
  .card--back  { left: 42px; top: 617px; }

  .brand-name {
    position: absolute;
    color: var(--sage);
    font-weight: 700;
    text-transform: uppercase;
    white-space: nowrap;
    line-height: 1;
  }
  .card--front .brand-name {
    left: 50%;
    top: 138px;
    transform: translateX(-50%);
    font-size: 34px;
    letter-spacing: 6px;
  }
  .card--back .brand-name {
    left: 180px;
    top: 210px;
    transform: translateX(-50%);
    font-size: 20px;
    letter-spacing: 3.5px;
  }

  .meadow {
    position: absolute;
    left: 0;
    right: 0;
    bottom: 0;
    height: 130px;
    background: linear-gradient(to bottom, var(--sage-soft) 0%, var(--sage) 26%, var(--sage) 100%);
  }

  .holder-name {
    position: absolute;
    left: 596px;
    top: 116px;
    transform: translateX(-50%);
    color: var(--sage);
    font-size: 34px;
    font-weight: 800;
    letter-spacing: 1.5px;
    text-transform: uppercase;
    white-space: nowrap;
    line-height: 1;
  }
  .name-rule {
    position: absolute;
    left: 397px;
    top: 176px;
    width: 400px;
    height: 4px;
    background: var(--sage);
  }
  .contact-list {
    position: absolute;
    left: 485px;
    top: 233px;
    list-style: none;
    color: var(--sage);
    font-size: 12px;
    font-weight: 800;
    letter-spacing: 0.8px;
    text-transform: uppercase;
    line-height: 16px;
  }
  .contact-item {
    display: flex;
    align-items: flex-start;
    margin-bottom: 14px;
  }
  .contact-icon {
    width: 16px;
    height: 16px;
    margin-right: 10px;
    fill: var(--sage);
    flex: none;
  }
</style>
</head>
<body>
<main class="canvas">

  <section class="card card--front" aria-label="Business card front">
    <p class="brand-name">Wrenfield Acres</p>
    <div class="meadow" role="img" aria-label="Silhouette of a grassy meadow along the bottom of the card"></div>
  </section>

  <section class="card card--back" aria-label="Business card back">
    <p class="brand-name">Wrenfield Acres</p>

    <h1 class="holder-name">Danielle Hoskins</h1>
    <div class="name-rule"></div>

    <ul class="contact-list">
      <li class="contact-item">
        <svg class="contact-icon" viewBox="0 0 16 16" aria-hidden="true">
          <path d="M4.2 1c.5 0 .8.3 1 .7l1.1 2.6c.2.5 0 1-.4 1.3l-1 .7c.8 1.7 1.9 3 3.4 3.9l.8-.9c.4-.4.9-.5 1.3-.3l2.5 1.2c.4.2.6.6.6 1v1.6c0 .7-.6 1.3-1.3 1.2C6.6 13.5 2.6 9.300 2.3 2.4 2.3 1.6 2.8 1 3.5 1h.7z"/>
        </svg>
        <span>30 412 6638</span>
      </li>
      <li class="contact-item">
        <svg class="contact-icon" viewBox="0 0 16 16" aria-hidden="true">
          <path d="M8 0.5C5 0.5 2.8 2.8 2.8 5.7c0 3.8 5.2 9.8 5.2 9.8s5.2-6 5.2-9.8C13.2 2.8 11 0.5 8 0.5zm0 7.3a2.1 2.1 0 1 1 0-4.2 2.1 2.1 0 0 1 0 4.2z"/>
        </svg>
        <span>2716 Wrenfield Rd,<br>Alder Springs, CO 80544</span>
      </li>
      <li class="contact-item">
        <svg class="contact-icon" viewBox="0 0 16 16" aria-hidden="true">
          <path d="M1 3.5h14v1L8 9 1 4.5z"/>
          <path d="M1 6l7 4.5L15 6v6.5H1z"/>
        </svg>
        <span>danielle@wrenfieldacres.com</span>
      </li>
    </ul>
  </section>

</main>
</body>
</html>
```